Poster for Martial Arts Academy.

We need a poster that will attract new members to our martial arts gym. We have a new enrollment in January. We need a poster that looks cool at the same time looks serious and safe.

We are an Academy of martial arts that offer Yoga, BJJ, MMA, SW and THAIBOXING.

We will be using A3 size paper.

Target Market(s)

everybody.

Industry/Entity Type

Gym

Requirements
Must have
• Our logo
Velkommen til Norges største kampsportsenter

MMA - Brasiliansk Jiu jitsu - Submission Wrestling - Thaiboksing

Oppstart nybegynnerkurs 20 januar 2014.

Kom innom for en gratis prøvetime fra 17:00 hverdager.

Sørhagaveien 48
1389 Vekre

Facebook logo
Instagram logo
Twitter logo
www.dravikstudio.no

Kontakt: 931 48 275 - 958 23 604

```html
<!DOCTYPE html>
<html lang="no">
<head>
<meta charset="utf-8">
<title>Dravik Studio – Enroll in January</title>
<link href="https://fonts.googleapis.com/css2?family=Exo+2:ital,wght@0,500;0,700;1,800&display=swap" rel="stylesheet">
<style>
  :root {
    --sky-top: #e3ecef;
    --sky-mid: #f3f3ea;
    --cloud: #f7f7f4;
    --deck-light: #c9c9c6;
    --deck-dark: #9d9e9c;
    --figure: #2a2a2a;
    --skin: #c99a7c;
    --wave-blue: rgba(62, 102, 172, 0.82);
    --ink: #1e1e1e;
    --ink-soft: #3a3f47;
    --accent: #2f8fd6;
    --white: #ffffff;
  }
  html, body {
    margin: 0;
    padding: 0;
    overflow: hidden;
    background: #ffffff;
  }
  .poster {
    position: relative;
    width: 849px;
    height: 1200px;
    overflow: hidden;
    font-family: "Exo 2", sans-serif;
  }
  .hero-photo {
    position: absolute;
    inset: 0;
    background:
      linear-gradient(180deg, transparent 0 884px, var(--deck-light) 884px, var(--deck-dark) 1200px),
      radial-gradient(ellipse 520px 140px at 300px 780px, var(--cloud) 0%, rgba(247,247,244,0) 100%),
      linear-gradient(180deg, var(--sky-top) 0%, var(--sky-mid) 45%, #e8eef0 72%, #eef1f1 100%);
  }
  .hero-figure {
    position: absolute;
    left: 360px;
    top: 330px;
    width: 170px;
    height: 720px;
    border-radius: 80px 80px 40px 40px;
    background: linear-gradient(180deg, var(--skin) 0 36%, var(--figure) 36% 100%);
    opacity: 0.55;
  }
  .brand {
    position: absolute;
    top: 28px;
    left: 0;
    width: 100%;
    display: flex;
    flex-direction: column;
    align-items: center;
    gap: 22px;
  }
  .brand-mark {
    width: 120px;
    height: 120px;
    border-radius: 50%;
    background: var(--accent);
  }
  .brand-name {
    font-weight: 700;
    font-size: 54px;
    letter-spacing: 4px;
    color: var(--ink);
    margin: 0;
    line-height: 1;
  }
  .info {
    position: absolute;
    color: var(--ink-soft);
    font-weight: 500;
    font-size: 15px;
    line-height: 1.45;
    margin: 0;
  }
  .info strong { font-weight: 700; color: var(--ink); }
  .info-welcome {
    left: 28px;
    top: 372px;
    width: 300px;
  }
  .info-welcome .info-lead {
    font-weight: 700;
    font-size: 19px;
    color: var(--ink);
    margin: 0 0 6px;
    line-height: 1.2;
  }
  .info-welcome p { margin: 0; }
  .info-details {
    right: 28px;
    top: 610px;
    width: 230px;
    text-align: right;
  }
  .info-details p { margin: 0 0 10px; }
  .social {
    display: flex;
    justify-content: flex-end;
    gap: 8px;
    margin-top: 4px;
  }
  .social-dot {
    width: 22px;
    height: 22px;
    border-radius: 50%;
    background: var(--ink-soft);
  }
  .wave {
    position: absolute;
    left: 0;
    top: 0;
  }
  .offer {
    position: absolute;
    left: 0;
    width: 100%;
    text-align: center;
    color: var(--white);
    font-style: italic;
    font-weight: 800;
    margin: 0;
    text-shadow: 0 2px 4px rgba(0, 0, 0, 0.35);
  }
  .offer-headline {
    top: 1004px;
    font-size: 50px;
    letter-spacing: 2px;
  }
  .offer-classes {
    top: 1083px;
    font-size: 22px;
    letter-spacing: 1.5px;
    font-variant: small-caps;
  }
  .offer-web {
    top: 1146px;
    font-size: 17px;
    letter-spacing: 1.5px;
    text-transform: uppercase;
  }
</style>
</head>
<body>
<main class="poster">
  <div class="hero-photo" role="img" aria-label="Photo of a barefoot martial artist in black pants performing a high side kick on a wooden deck against a sky with clouds"></div>
  <div class="hero-figure" role="img" aria-label="Martial artist performing a side kick"></div>

  <header class="brand">
    <div class="brand-mark"></div>
    <h1 class="brand-name">DRAVIK STUDIO</h1>
  </header>

  <section class="info info-welcome">
    <p class="info-lead">Velkommen til Norges største kampsportsenter</p>
    <p>MMA - Brasiliansk Jiu jitsu - Submission Wrestling - Thaiboksing</p>
  </section>

  <section class="info info-details">
    <p><strong>Oppstart nybegynnerkurs 20 januar 2014.</strong></p>
    <p>Kom innom for en gratis prøvetime fra 17:00 hverdager.</p>
    <p>Sørhagaveien 48<br>1389 Vekre</p>
    <p>Kontakt: 931 48 275 - 958 23 604</p>
    <p>www.dravikstudio.no</p>
    <div class="social" aria-label="Sosiale medier">
      <span class="social-dot"></span>
      <span class="social-dot"></span>
      <span class="social-dot"></span>
    </div>
  </section>

  <svg class="wave" width="849" height="1200" viewBox="0 0 849 1200" aria-hidden="true">
    <path d="M0,1022 C260,1018 560,1000 849,890 L849,1200 L0,1200 Z" fill="var(--wave-blue)"/>
  </svg>

  <p class="offer offer-headline">ENROLL IN JANUARY!</p>
  <p class="offer offer-classes">Yoga, BJJ, MMA, SW and THAIBOXING</p>
  <p class="offer offer-web">www.dravikkamp.com</p>
</main>
</body>
</html>
```